Lydia Vandermere personal business/name cards and stationery brief

I am looking for a simple design on my personal business cards, that I may use for all my stationery. All my stationery would be cream or ivory textured card, or cream/ivory quality paper. I am director of my family company and also property developer. But am wishing to have basic business cards that I can use across both businesses. I do not wish to have a title, just my initials as a focal point.
Target Market(s)
These are my personal business cards and stationery. I am looking for an elegant, relatively understated design that exudes wealth. There is no target audience, other than clients or people I already do business with. However design must be stylish and timeless.
If I am handing out my business card to anyone I do not do business with, or they are not contracting to me or my company currently, then i would like the target audience to wish they were.
I am 54 yeas of age, and my business cards must denote respect and class.
Industry/Entity Type
Business
Contact Information for Business Card
LV
Lydia Vandermere
Justice of the Peace
Possible rear of card
Mobile number
Email
Font styles to use
Requirements
Must have
- LV to be somehow entwined as a logo on the front of the card above my name
- These cards must state that I am a Justice of the Peace
- Colours only ivory or cream card with texture, and gold elegant font.
- Must be able to be used on all my stationery products
- Must be elegant, timeless and not cluttered
- Below are just some design I like. There is something in each design I like.
Nice to have
- I would like my initials to be the centre piece of the card. Somehow entwined together elegantly in a logo of sorts that I can use across all my stationery. But if not my initials, then something that is different and stands out from the rest.
Should not have
- Not gawdy or young. No colour. Nothing outlandish.

```html
<!DOCTYPE html>
<html lang="en">
<head>
<meta charset="utf-8">
<title>Lydia Vandermere – Business Card</title>
<link rel="stylesheet" href="https://fonts.googleapis.com/css2?family=Cinzel:wght@400;500&family=Quattrocento:wght@400&family=Roboto:wght@400&display=swap">
<style>
  :root {
    --backdrop: #72706e;
    --card-ivory: #fefee9;
    --gold: #c9a53a;
    --gold-faint: #f4ecc4;
    --ink: #363636;
    --ink-soft: #4a4a4a;
  }
  * { box-sizing: border-box; margin: 0; padding: 0; }
  html, body {
    width: 1200px;
    height: 484px;
    overflow: hidden;
    background: var(--backdrop);
  }
  .stage {
    position: relative;
    width: 1200px;
    height: 484px;
  }
  .card {
    position: absolute;
    top: 106px;
    width: 452px;
    height: 272px;
    background: var(--card-ivory);
    overflow: hidden;
  }
  .card--front { left: 130px; }
  .card--back { left: 617px; }

  .monogram {
    position: absolute;
    left: 0;
    right: 0;
    top: 50%;
    transform: translateY(-50%);
    text-align: center;
    font-family: "Cinzel", serif;
    font-weight: 400;
    font-size: 110px;
    line-height: 1;
    letter-spacing: 4px;
    color: var(--gold);
  }
  .monogram--faint {
    top: 134px;
    font-size: 120px;
    color: var(--gold-faint);
  }

  .details {
    position: absolute;
    left: 0;
    right: 0;
    top: 0;
    text-align: center;
  }
  .details__name {
    position: absolute;
    left: 0; right: 0;
    top: 86px;
    font-family: "Cinzel", serif;
    font-weight: 500;
    font-size: 23px;
    letter-spacing: 1.2px;
    color: var(--ink);
    line-height: 1.2;
  }
  .details__role {
    position: absolute;
    left: 0; right: 0;
    top: 119px;
    font-family: "Roboto", sans-serif;
    font-size: 11.5px;
    color: var(--ink);
  }
  .details__contact {
    position: absolute;
    left: 0; right: 0;
    font-family: "Quattrocento", serif;
    font-size: 11.5px;
    color: var(--ink-soft);
  }
  .details__phone { top: 150px; }
  .details__email { top: 166px; }
</style>
</head>
<body>
  <main class="stage">
    <section class="card card--front" aria-label="Card front">
      <div class="monogram">LV</div>
    </section>

    <section class="card card--back" aria-label="Card back">
      <div class="monogram monogram--faint" aria-hidden="true">LV</div>
      <div class="details">
        <h1 class="details__name">LYDIA VANDERMERE</h1>
        <p class="details__role">Justice of the Peace</p>
        <p class="details__contact details__phone">12-555-0148</p>
        <p class="details__contact details__email">lydia@vandermerehouse.com.au</p>
      </div>
    </section>
  </main>
</body>
</html>
```